Facebook Fan Page for Kestro Vane, EDM DJ!

I just got a new logo because I plan a reboot in my DJ Career. This also includes a new visual identity in all categories. So in social media. I need a title picture and a profile pic which represent my alias as EDM-DJ. Both should be usable in facebook and twitter as well. It can not be necessary. The graphics should represent my favorite music styles in EDM for example: House, Electro, Electro House, Melbourne Bounce and Big Room. The design should match the new logo which I attached to the project description.

Target Market(s)

Young people who love electronic music and DJ mixes.

Industry/Entity Type

Media

Colors

Designer to choose colors to be used in the design.

Requirements
Must have
• I definitely need graphics to represent my logo and what I'm doing. It should be fit together.
Nice to have
• Complete background design for the facebook and twitter page. Nice to have but not necessary. Maybe implied dj gear in an abstract way.
Should not have
• Funny pictures and a playful or childish appearance. No golden elements.

```html
<!DOCTYPE html>
<html lang="en">
<head>
<meta charset="utf-8">
<title>Kestro Vane – EDM DJ Social Set</title>
<link rel="stylesheet" href="https://fonts.googleapis.com/css2?family=Russo+One&display=swap">
<style>
  :root {
    --stage: #1c1c1e;
    --deep-blue: #2b2a8c;
    --violet: #5a2a9a;
    --magenta: #c0338f;
    --panel: #2a0f3a;
    --panel-edge: #6b2a7e;
    --line: rgba(255, 210, 245, 0.55);
    --chrome: #e9c8e4;
    --chrome-dark: #b9a8c2;
    --brand-blue: #2f86ff;
    --black: #000000;
    --white: #ffffff;
  }
  html, body {
    margin: 0;
    padding: 0;
    width: 1200px;
    height: 1200px;
    overflow: hidden;
    background: var(--stage);
  }
  .canvas {
    position: relative;
    width: 1200px;
    height: 1200px;
  }
  .cover {
    position: absolute;
    left: 80px;
    top: 230px;
    width: 1040px;
    height: 390px;
    box-shadow: 0 10px 30px rgba(0,0,0,0.6);
  }
  .cover svg { display: block; }
  .cover-name {
    font-family: "Russo One", sans-serif;
    font-size: 34px;
    fill: var(--brand-blue);
  }
  .cover-title {
    font-family: "Russo One", sans-serif;
    font-size: 210px;
    fill: url(#chrome);
    letter-spacing: 4px;
  }
  .cover-sub {
    font-family: "Russo One", sans-serif;
    font-size: 96px;
    fill: var(--chrome-dark);
    letter-spacing: 4px;
  }
  .profile {
    position: absolute;
    left: 80px;
    top: 690px;
    width: 260px;
    height: 260px;
    box-sizing: border-box;
    border: 4px solid var(--white);
    background: var(--black);
    display: flex;
    align-items: center;
    justify-content: center;
    box-shadow: 0 0 0 1px rgba(0,0,0,0.3);
  }
  .profile-name {
    font-family: "Russo One", sans-serif;
    font-size: 30px;
    color: var(--brand-blue);
    margin: 0;
  }
</style>
</head>
<body>
<main class="canvas">
  <section class="cover" aria-label="Cover image">
    <svg width="1040" height="390" viewBox="0 0 1040 390" xmlns="http://www.w3.org/2000/svg">
      <defs>
        <radialGradient id="glow" cx="50%" cy="30%" r="70%">
          <stop offset="0" stop-color="var(--magenta)"/>
          <stop offset="0.55" stop-color="var(--violet)"/>
          <stop offset="1" stop-color="var(--deep-blue)"/>
        </radialGradient>
        <linearGradient id="chrome" x1="0" y1="0" x2="0" y2="1">
          <stop offset="0" stop-color="#f5e6f2"/>
          <stop offset="0.5" stop-color="var(--chrome)"/>
          <stop offset="1" stop-color="#8d5f93"/>
        </linearGradient>
      </defs>
      <rect class="cover-backdrop" width="1040" height="390" fill="url(#glow)" role="img" aria-label="Glowing hexagon mesh backdrop in violet and magenta"/>
      <g class="cover-lines" stroke="var(--line)" stroke-width="1.2" fill="none">
        <line x1="106" y1="0" x2="106" y2="390"/>
        <line x1="934" y1="0" x2="934" y2="390"/>
        <polyline points="240,0 55,180 240,390"/>
        <polyline points="800,0 985,180 800,390"/>
        <line x1="260" y1="0" x2="430" y2="390"/>
        <line x1="780" y1="0" x2="610" y2="390"/>
      </g>
      <polygon class="cover-panel" points="345,0 695,0 749,70 749,290 690,390 350,390 291,290 291,70"
               fill="var(--panel)" stroke="var(--panel-edge)" stroke-width="2"/>
      <text class="cover-name" x="520" y="44" text-anchor="middle">KESTRO VANE</text>
      <text class="cover-title" x="520" y="284" text-anchor="middle">EDM</text>
      <text class="cover-sub" x="520" y="378" text-anchor="middle">DJ</text>
    </svg>
  </section>

  <section class="profile" aria-label="Profile picture">
    <p class="profile-name">KESTRO VANE</p>
  </section>
</main>
</body>
</html>
```